Health Wellbeing Beauty online Shop

I have attached a full spec, however in summary this is a new business startup selling skincare products.

We need a web design for new wellbeing website, selling skincare products so need an eCommerce solution . On the home page I would like these faces to dissolve into each other on a loop or use a honeycomb style transation.
You will need the option of being able to log into an account, either through chatterbook, quorvix, pipsqueal or create an account. For created accounts, obviously need the facility to be able to reset passwords, see previous orders, track current order, and maintain favourites.
It should be PC, mobile and tablet friendly.

Look and Feel
It should be an elegant, modern, professional, trendy, unisex website. It should look clean and calm. Am happy to try interesting and slightly unusual designs. I would also like to have chat functionality, either powered by ravUNtalk or by Oxa 17.
Websites I like are
https://www.novel-radiance.co.uk/
https://www.merelytonics.co.uk/
http://www.glowdermara.com/

PLEASE DO USE YOUR KNOWELDGE OF WHAT WORKS FOR WEB DESIGN. YOU’RE THE EXPERT AND NEED YOUR EXPERTISE. CARTE BLANCHE TO DESIGN AS YOU SEE FIT. Please be creative, I need my site to stand out from the crowd.

Target Market(s)

Target Market
Middle aged women are our most common client, however, younger patients, both male and female, will often visit the site. In summary, I would like the site to appeal to all age brackets.

Industry/Entity Type

Business

Coding

Coded - Design and coding required

Number of Pages Required

4 page

Requirements
Must have
• Need shop to be exactly like shop on this link http://www.glowdermara.com/
Nice to have
• i would like something unique and creative

```html
<!DOCTYPE html>
<html lang="en">
<head>
<meta charset="utf-8">
<title>Velora Skin Clinic</title>
<link href="https://fonts.googleapis.com/css2?family=Open+Sans:wght@400;600;700&family=Dancing+Script:wght@700&display=swap" rel="stylesheet">
<style>
:root{
  --gold:#e0c66b;
  --gold-text:#d3a737;
  --gold-dark:#c9a94a;
  --ink:#2f2f2f;
  --muted:#6b6b6b;
  --light:#f3f3f3;
  --line:#e2e2e2;
  --footer:#474a52;
  --footer-line:#5a5d65;
  --footer-text:#e9e9e9;
  --sale:#e0161b;
  --new:#2bb52b;
}
*{box-sizing:border-box;margin:0;padding:0}
html,body{width:1200px;height:2744px;overflow:hidden}
body{font-family:'Open Sans',Arial,sans-serif;color:var(--ink);background:#fff;position:relative}
.abs{position:absolute}
svg{display:block}

/* top bar */
.topbar{top:0;left:0;width:1200px;height:33px;border-bottom:1px solid var(--line)}
.topbar span{position:absolute;top:10px;font-size:10px;color:#444;display:flex;align-items:center;gap:4px}
/* header */
.header{top:33px;left:0;width:1200px;height:62px}
.brand{left:155px;top:6px;display:flex;align-items:center;gap:10px;font-size:22px;font-weight:600;color:var(--ink)}
.brand i{width:40px;height:40px;border:1.5px solid var(--ink);border-radius:50%}
.nav{left:357px;top:0;height:62px;display:flex;align-items:stretch;font-size:11.5px;font-weight:600}
.nav a{display:flex;align-items:center;padding:0 13px;color:#333;text-decoration:none}
.nav a.active{background:var(--gold);color:#fff;padding:0 14px}
.cart{left:964px;top:18px;display:flex;align-items:center;gap:8px;font-size:11.5px;font-weight:600;border-left:1px solid var(--line);padding-left:14px;height:26px}

/* hero */
.hero{top:95px;left:0;width:1200px;height:360px;background:var(--light)}
.hero-photo{left:622px;top:0;width:360px;height:360px;background:radial-gradient(ellipse at 50% 45%,#f0d9c4 0%,#e6c29f 35%,#eed9c6 60%,var(--light) 80%)}
.hero h1{left:157px;top:86px;font-size:31px;font-weight:600;letter-spacing:.5px;color:#333}
.hero p{left:157px;top:140px;width:460px;font-size:11.5px;line-height:17px;color:#555}
.btn{display:inline-flex;align-items:center;justify-content:center;gap:6px;background:var(--gold);color:#333;font-size:11.5px;font-weight:600;box-shadow:3px 3px 0 var(--gold-dark)}
.hero .btn{position:absolute;left:157px;top:222px;width:126px;height:33px}
.arrow{top:155px}

/* welcome */
.welcome{top:455px;left:0;width:1200px;height:240px;text-align:center}
.welcome h2{position:absolute;top:42px;width:100%;font-size:20px;font-weight:600}
.welcome h2 em{font-style:normal;color:var(--gold-text)}
.welcome p{position:absolute;top:92px;left:240px;width:720px;font-size:11.5px;line-height:19px;color:#555}
.welcome .btn{position:absolute;left:536px;top:180px;width:128px;height:35px}

/* promo grid */
.tile{background:var(--light)}
.tile .photo{position:absolute}
.tile h3{position:absolute;font-size:21px;font-weight:400;color:var(--gold-text)}
.tile p{position:absolute;font-size:11px;color:#666}
.tile.dark h3{color:#333;font-size:19px}
.savings{background:#fdeca0}
.savings .frame{position:absolute;left:14px;top:14px;right:14px;bottom:14px;border:1px solid #e2c45b}
.savings b{position:absolute;top:40px;width:100%;text-align:center;font-family:'Dancing Script',cursive;font-size:34px;color:#222}
.savings span{position:absolute;top:92px;width:100%;text-align:center;font-size:13px;color:#333}

/* product tabs */
.tabs{top:1311px;left:155px;width:890px;height:37px}
.tabs .label{position:absolute;left:0;top:0;width:128px;height:37px;background:var(--gold);font-size:12px;font-weight:600;display:flex;align-items:center;justify-content:center}
.tabs .list{position:absolute;left:147px;top:0;width:680px;height:37px;border:1px solid var(--line);display:flex;align-items:center;gap:33px;padding-left:22px;font-size:11.5px}
.tabs .list .on{color:var(--gold-text)}
.tabs .nav-btn{position:absolute;top:0;width:21px;height:37px;background:var(--gold);display:flex;align-items:center;justify-content:center}

.card{top:1370px;width:205px;height:327px;border:1px solid var(--line);background:#fff;text-align:center}
.card.hover{box-shadow:0 0 8px rgba(0,0,0,.15)}
.card .img{position:absolute;left:8px;top:8px;width:187px;height:144px}
.card.hover .img{background:#f0f0f0}
.card .bottle{position:absolute;left:50%;transform:translateX(-50%);border-radius:4px}
.card h4{position:absolute;top:160px;width:100%;font-size:14px;font-weight:600}
.card.hover h4{color:var(--gold-text);font-weight:400}
.card .stars{position:absolute;top:183px;width:100%;font-size:10px;color:#f0a400;letter-spacing:1px}
.card .stars s{text-decoration:none;color:#ccc}
.card p{position:absolute;top:200px;left:14px;width:175px;font-size:10.5px;line-height:15px;color:#555}
.card .price{position:absolute;top:250px;width:100%;font-size:12px;color:var(--gold-text)}
.card .price del{color:#888;margin-right:4px}
.card .acts{position:absolute;top:284px;width:100%;display:flex;justify-content:center;gap:10px}
.card .acts i{width:23px;height:23px;border-radius:50%;border:1px solid var(--line);display:flex;align-items:center;justify-content:center}
.card.hover .acts i{background:#3b3b3b;border-color:#3b3b3b}
.badge{top:-2px;left:-4px;width:50px;height:24px;color:#fff;font-size:11px;display:flex;align-items:center;justify-content:center}

/* feature band */
.feature{top:1747px;left:0;width:1200px;height:265px;border-top:1px solid var(--line);border-bottom:1px solid var(--line)}
.feature .photo{position:absolute;left:0;top:0;width:600px;height:265px;background:linear-gradient(90deg,#f4f3f2 0%,#e9e2dc 35%,#c9a58a 50%,#ede7e2 68%,#f6f5f4 100%)}
.feature h3{position:absolute;left:664px;top:42px;width:340px;font-size:14px;font-weight:700;line-height:20px}
.feature p{position:absolute;left:664px;top:100px;width:380px;font-size:11px;line-height:20px;color:#555}
.feature .btn{position:absolute;left:664px;top:186px;width:126px;height:35px}

/* newsletter */
.newsletter{top:2063px;left:0;width:1200px;height:238px;background:#f6f6f6;text-align:center}
.newsletter h2{position:absolute;top:57px;width:100%;font-size:17px;font-weight:700;letter-spacing:.5px}
.newsletter p{position:absolute;top:93px;left:380px;width:440px;font-size:10.5px;line-height:15px;font-style:italic;color:#444}
.newsletter .field{position:absolute;left:360px;top:137px;width:481px;height:35px;background:#fff;border:1px solid #ddd;box-shadow:2px 2px 0 #e1e1e1;display:flex;align-items:center;justify-content:space-between;padding:0 16px;font-size:10.5px;font-style:italic;color:#555}

/* footer */
.footer{top:2301px;left:0;width:1200px;height:443px;background:var(--footer);color:var(--footer-text)}
.perk{position:absolute;top:30px;display:flex;align-items:center;gap:14px}
.perk i{width:52px;height:52px;border-radius:50%;border:2px solid #6a6d74;display:flex;align-items:center;justify-content:center}
.perk b{display:block;font-size:11.5px;font-weight:600}
.perk small{display:block;font-size:10px;color:#9a9ca2;margin-top:2px}
.rule{left:155px;width:890px;height:1px;background:var(--footer-line)}
.col{position:absolute;top:146px}
.col h5{font-size:14px;font-weight:700;color:var(--gold);letter-spacing:.5px}
.col h5:after{content:"";display:block;width:36px;height:2px;background:var(--gold);margin-top:7px}
.col ul{list-style:none;margin-top:18px}
.col li{font-size:11.5px;height:21px;display:flex;align-items:center;gap:10px}
.col li:before{content:"»";color:var(--gold);font-size:13px}
.col li.on{color:var(--gold)}
.col.contact li:before{content:none}
.col.contact li{align-items:flex-start;height:auto;margin-bottom:6px;line-height:17px}
.copy{left:155px;top:2696px;font-size:10.5px}
.copy em{font-style:normal;color:var(--gold)}
.pay{top:2690px;display:flex;gap:6px;left:829px}
.pay i{width:34px;height:22px;border-radius:3px;background:#e8e8e8}
</style>
</head>
<body>

<!-- top bar -->
<div class="abs topbar">
  <span style="left:644px"><svg width="10" height="10" viewBox="0 0 10 10"><circle cx="5" cy="5" r="4" fill="none" stroke="#444"/></svg>English ▾</span>
  <span style="left:744px">$ USD ▾</span>
  <span style="left:801px"><svg width="9" height="10" viewBox="0 0 9 10"><circle cx="4.5" cy="3" r="2.5" fill="#444"/><path d="M0 10c0-3 2-4.5 4.5-4.5S9 7 9 10z" fill="#444"/></svg>My Account ▾</span>
  <span style="left:909px"><svg width="9" height="10" viewBox="0 0 9 10"><rect x="0" y="4" width="9" height="6" fill="#444"/><path d="M2 4V3a2.5 2.5 0 015 0v1" fill="none" stroke="#444" stroke-width="1.3"/></svg>Sign In</span>
  <span style="left:982px"><svg width="10" height="9" viewBox="0 0 10 9"><path d="M5 9L1 5a2.3 2.3 0 014-3 2.3 2.3 0 014 3z" fill="#444"/></svg>Wish List</span>
</div>

<!-- header -->
<header class="abs header">
  <div class="abs brand"><i></i>Velora</div>
  <nav class="abs nav">
    <a class="active">Home</a><a>About Us</a><a>Tablets</a><a>Creams</a><a>Soaps</a><a>Vials</a><a>Shop</a><a>Contact Us</a>
    <a><svg width="11" height="11" viewBox="0 0 11 11"><circle cx="4.5" cy="4.5" r="3.5" fill="none" stroke="#333" stroke-width="1.6"/><path d="M7 7l3.5 3.5" stroke="#333" stroke-width="1.8"/></svg></a>
  </nav>
  <div class="abs cart">
    <svg width="20" height="16" viewBox="0 0 20 16"><path d="M1 5h18l-2 10H3z" fill="var(--gold)"/><path d="M6 5l3-4M14 5l-3-4" stroke="var(--gold)" stroke-width="1.5"/></svg>
    (3 items)
  </div>
</header>

<!-- hero -->
<section class="abs hero">
  <div class="abs hero-photo" role="img" aria-label="Smiling woman with short blonde hair touching her face"></div>
  <h1 class="abs">Donec quam placerat ristique</h1>
  <p class="abs">Abitant morbi tristique senectus eft netus eft malesuada fames ac turpis egestas enean non tellDonec pede quam placerat ristique faucibus poserw uete lobortid Lorem ipsum.</p>
  <a class="btn">View More <span>›</span></a>
  <svg class="abs arrow" style="left:106px" width="24" height="50" viewBox="0 0 24 50"><path d="M22 2L2 25l20 23" fill="none" stroke="#cfcfcf" stroke-width="1.5"/></svg>
  <svg class="abs arrow" style="left:1068px" width="24" height="50" viewBox="0 0 24 50"><path d="M2 2l20 23L2 48" fill="none" stroke="var(--gold)" stroke-width="1.5"/></svg>
</section>

<!-- welcome -->
<section class="abs welcome">
  <h2>Welcome to <em>Velora Skin Clinic</em></h2>
  <p>Occaecati cupiditate non provident, similique sunt in culpa qui officia deserunt mollitia animi, id est laborum et dolorum fuga. Et harum quidem rerum facilis est et expedita distinctio. Lorem ipsum dolor sit amet, consectetur adipiscing elit. Maecenas id est sed lacus volutpat lobortis.</p>
  <a class="btn">View More <span>›</span></a>
</section>

<!-- promo grid -->
<div class="abs tile" style="left:155px;top:719px;width:586px;height:159px">
  <div class="photo" role="img" aria-label="Assorted skincare bottles and makeup compacts" style="left:0;top:6px;width:150px;height:150px;background:linear-gradient(90deg,#d9d4cf,#8a7d72 45%,#c9c2bb)"></div>
  <h3 style="left:272px;top:48px">Skin Lightening Products</h3>
  <p style="left:272px;top:86px">You are going to use a passage.</p>
</div>
<div class="abs tile" style="left:763px;top:719px;width:282px;height:360px">
  <div class="photo" role="img" aria-label="Group of white skincare bottles" style="left:65px;top:20px;width:150px;height:200px;background:radial-gradient(ellipse at center,#d8d8dc 0%,#ececee 55%,var(--light) 75%)"></div>
  <h3 style="left:0;width:100%;text-align:center;top:260px;font-size:18px;color:#777">Skin Lightening Products</h3>
  <p style="right:20px;top:301px">You are going to use a passage.</p>
</div>
<div class="abs tile dark" style="left:155px;top:902px;width:282px;height:360px">
  <h3 style="left:0;width:100%;text-align:center;top:30px">Skin Lightening Products</h3>
  <p style="left:0;width:100%;text-align:center;top:63px;line-height:14px">You are going to use<br>a passage.</p>
  <div class="photo" role="img" aria-label="Pink perfume bottle and foundation jars" style="left:50px;top:125px;width:190px;height:225px;background:linear-gradient(160deg,#f2dde4 0%,#e4a3b8 40%,#d9b37c 70%,#f1ece6 100%)"></div>
</div>
<div class="abs savings" style="left:459px;top:902px;width:282px;height:177px">
  <div class="frame"></div>
  <b>Big Savings</b>
  <span>Up to 20% Discount</span>
</div>
<div class="abs tile" style="left:459px;top:1103px;width:586px;height:159px">
  <h3 style="left:30px;top:52px;font-size:22px">Skin Lightening Products</h3>
  <p style="left:30px;top:91px">You are going to use a passage.</p>
  <div class="photo" role="img" aria-label="Silver cream jar and tall bottle" style="left:380px;top:0;width:190px;height:159px;background:radial-gradient(ellipse at center,#b9b9bd 0%,#dcdcde 45%,var(--light) 75%)"></div>
</div>

<!-- product tabs -->
<div class="abs tabs">
  <div class="label">New Products</div>
  <div class="list"><span>Skin Lightening Tablets</span><span class="on">Skin Lightening Creams</span><span>Skin Lightening Soaps</span><span>Skin Lightening Vials</span></div>
  <div class="nav-btn" style="left:845px"><svg width="7" height="11" viewBox="0 0 7 11"><path d="M6 1L1.5 5.5 6 10" fill="none" stroke="#fff" stroke-width="1.6"/></svg></div>
  <div class="nav-btn" style="left:869px"><svg width="7" height="11" viewBox="0 0 7 11"><path d="M1 1l4.5 4.5L1 10" fill="none" stroke="#fff" stroke-width="1.6"/></svg></div>
</div>

<!-- product cards -->
<div class="abs card" style="left:155px">
  <div class="img" role="img" aria-label="White serum bottle"><div class="bottle" style="top:22px;width:30px;height:100px;background:linear-gradient(90deg,#d4d4d4,#fafafa,#cfcfcf)"></div></div>
  <div class="abs badge" style="background:var(--sale)">Sale</div>
  <h4>Lorium Ipum name</h4>
  <div class="stars">★★★★<s>★</s></div>
  <p>Lorem ipsum dolor sit amet conse ctetur adipiscing elit, sed-do eiusmod tempor incididunt.</p>
  <div class="price"><del>$150</del>$100</div>
  <div class="acts"><i><svg width="10" height="9" viewBox="0 0 10 9"><path d="M5 9L1 5a2.3 2.3 0 014-3 2.3 2.3 0 014 3z" fill="#333"/></svg></i><i><svg width="11" height="10" viewBox="0 0 11 10"><path d="M0 1h2l1.5 6h6l1-4.5H3" fill="none" stroke="#333" stroke-width="1.2"/><circle cx="4" cy="9" r="1" fill="#333"/><circle cx="9" cy="9" r="1" fill="#333"/></svg></i><i><svg width="10" height="10" viewBox="0 0 10 10"><path d="M1 9L9 1M6 1h3v3M1 6v3h3" fill="none" stroke="#333" stroke-width="1.2"/></svg></i></div>
</div>
<div class="abs card hover" style="left:382px">
  <div class="img" role="img" aria-label="Pump bottle with silver cap"><div class="bottle" style="top:18px;width:28px;height:110px;background:linear-gradient(90deg,#cfcfcf,#fff,#c4c4c4)"></div></div>
  <h4>Lorium Ipum name</h4>
  <div class="stars">★★★★<s>★</s></div>
  <p>Lorem ipsum dolor sit amet conse ctetur adipiscing elit, sed-do eiusmod tempor incididunt.</p>
  <div class="price"><del>$140</del>$120</div>
  <div class="acts"><i><svg width="10" height="9" viewBox="0 0 10 9"><path d="M5 9L1 5a2.3 2.3 0 014-3 2.3 2.3 0 014 3z" fill="var(--gold)"/></svg></i><i><svg width="11" height="10" viewBox="0 0 11 10"><path d="M0 1h2l1.5 6h6l1-4.5H3" fill="none" stroke="var(--gold)" stroke-width="1.2"/><circle cx="4" cy="9" r="1" fill="var(--gold)"/><circle cx="9" cy="9" r="1" fill="var(--gold)"/></svg></i><i><svg width="10" height="10" viewBox="0 0 10 10"><path d="M1 9L9 1M6 1h3v3M1 6v3h3" fill="none" stroke="var(--gold)" stroke-width="1.2"/></svg></i></div>
</div>
<div class="abs card" style="left:611px">
  <div class="img" role="img" aria-label="Set of silver cream jars and bottles"><div class="bottle" style="top:40px;width:120px;height:70px;background:linear-gradient(90deg,#ddd,#9e9ea2 30%,#e8e8e8 55%,#a8a8ac 80%,#ddd)"></div></div>
  <div class="abs badge" style="background:var(--new)">New</div>
  <h4>Lorium Ipum name</h4>
  <div class="stars">★★★★<s>★</s></div>
  <p>Lorem ipsum dolor sit amet conse ctetur adipiscing elit, sed-do eiusmod tempor incididunt.</p>
  <div class="price"><del>$180</del>$150</div>
  <div class="acts"><i><svg width="10" height="9" viewBox="0 0 10 9"><path d="M5 9L1 5a2.3 2.3 0 014-3 2.3 2.3 0 014 3z" fill="#333"/></svg></i><i><svg width="11" height="10" viewBox="0 0 11 10"><path d="M0 1h2l1.5 6h6l1-4.5H3" fill="none" stroke="#333" stroke-width="1.2"/><circle cx="4" cy="9" r="1" fill="#333"/><circle cx="9" cy="9" r="1" fill="#333"/></svg></i><i><svg width="10" height="10" viewBox="0 0 10 10"><path d="M1 9L9 1M6 1h3v3M1 6v3h3" fill="none" stroke="#333" stroke-width="1.2"/></svg></i></div>
</div>
<div class="abs card" style="left:840px">
  <div class="img" role="img" aria-label="Foundation bottle with pump"><div class="bottle" style="top:22px;width:30px;height:100px;background:linear-gradient(180deg,#e9e4de,#e6c7a3 50%,#d8b48c)"></div></div>
  <h4>Lorium Ipum name</h4>
  <div class="stars">★★★★<s>★</s></div>
  <p>Lorem ipsum dolor sit amet conse ctetur adipiscing elit, sed-do eiusmod tempor incididunt.</p>
  <div class="price"><del>$135</del>$105</div>
  <div class="acts"><i><svg width="10" height="9" viewBox="0 0 10 9"><path d="M5 9L1 5a2.3 2.3 0 014-3 2.3 2.3 0 014 3z" fill="#333"/></svg></i><i><svg width="11" height="10" viewBox="0 0 11 10"><path d="M0 1h2l1.5 6h6l1-4.5H3" fill="none" stroke="#333" stroke-width="1.2"/><circle cx="4" cy="9" r="1" fill="#333"/><circle cx="9" cy="9" r="1" fill="#333"/></svg></i><i><svg width="10" height="10" viewBox="0 0 10 10"><path d="M1 9L9 1M6 1h3v3M1 6v3h3" fill="none" stroke="#333" stroke-width="1.2"/></svg></i></div>
</div>

<!-- feature band -->
<section class="abs feature">
  <div class="photo" role="img" aria-label="Woman with long curly auburn hair"></div>
  <h3>Nullam ullamcorper nisl quis ornare molestie</h3>
  <p>Claritas processus dynamicus sequitu consut, consut ryethm sirter smreted oeureots Claritas processus dynamicus sequitu consution Claritas processus dynamicus.</p>
  <a class="btn">View More <span>›</span></a>
</section>

<!-- newsletter -->
<section class="abs newsletter">
  <h2>SIGN UP TO NEWSLETTER</h2>
  <p>Subscribe to the cabinet group mailing list to receive updates on new arrivals, special offers and other discount information.</p>
  <div class="field"><span>Enter Your Email Address</span><svg width="14" height="13" viewBox="0 0 14 13"><path d="M0 6L14 0 10 13 7 8z" fill="#333"/></svg></div>
</section>

<!-- footer -->
<footer class="abs footer">
  <div class="perk" style="left:155px"><i><svg width="22" height="15" viewBox="0 0 22 15"><rect x="0" y="1" width="13" height="10" fill="#fff"/><path d="M13 4h5l3 4v3h-8z" fill="#fff"/><circle cx="5" cy="12.5" r="2" fill="#fff" stroke="var(--footer)"/><circle cx="17" cy="12.5" r="2" fill="#fff" stroke="var(--footer)"/></svg></i><div><b>Free shipping worldwide</b><small>On order over $200</small></div></div>
  <div class="perk" style="left:382px"><i><svg width="20" height="20" viewBox="0 0 20 20"><path d="M4 6a8 8 0 11-1 7" fill="none" stroke="#fff" stroke-width="2"/><path d="M1 2v6h6" fill="none" stroke="#fff" stroke-width="2"/><path d="M10 6v5l3 2" fill="none" stroke="#fff" stroke-width="1.6"/></svg></i><div><b>30 days free return</b><small>Money back guarantee</small></div></div>
  <div class="perk" style="left:611px"><i><svg width="20" height="20" viewBox="0 0 20 20"><rect x="1" y="8" width="4" height="11" fill="#fff"/><path d="M6 9l4-8c2 0 2.5 1.5 2 4h6a1.5 1.5 0 011.5 2l-2 10a1.5 1.5 0 01-1.5 1.5H6z" fill="#fff"/></svg></i><div><b>Member safe shopping</b><small>Safe shopping guarantee</small></div></div>
  <div class="perk" style="left:840px"><i><svg width="18" height="18" viewBox="0 0 18 18"><path d="M4 1l3 4-2 2a11 11 0 006 6l2-2 4 3-2 3C8 17 1 10 1 3z" fill="#fff"/></svg></i><div><b>+44 800 555 0199</b><small>Call with us</small></div></div>
  <div class="abs rule" style="top:113px"></div>

  <div class="col" style="left:155px"><h5>QUICK LINKS</h5><ul><li class="on">Home</li><li>About Us</li><li>Tablets</li><li>Creams</li><li>Soaps</li><li>Vials</li><li>Contact Us</li></ul></div>
  <div class="col" style="left:384px"><h5>MY ACCOUNT</h5><ul><li class="on">My Account</li><li>Wish List</li><li>Site Map</li><li>Custom Service</li><li>Custom Link</li><li>Payments</li><li>Returns</li></ul></div>
  <div class="col" style="left:613px"><h5>FAQ</h5><ul><li>Product Questions</li><li>Order Questions</li><li class="on">Subscription Questions</li><li>Payment Questions</li><li>Company Questions</li><li>Cart Questions</li><li>Returns Questions</li></ul></div>
  <div class="col contact" style="left:840px"><h5>CONTACT US</h5><ul>
    <li><svg width="11" height="11" viewBox="0 0 18 18"><path d="M4 1l3 4-2 2a11 11 0 006 6l2-2 4 3-2 3C8 17 1 10 1 3z" fill="var(--gold)"/></svg>Telephone: +44 800 555 0199</li>
    <li><svg width="12" height="10" viewBox="0 0 12 10"><rect x="0.5" y="0.5" width="11" height="9" fill="none" stroke="var(--gold)"/><path d="M0.5 0.5L6 5l5.5-4.5" fill="none" stroke="var(--gold)"/></svg>Email: hello@velora-mail.com</li>
    <li><svg width="12" height="12" viewBox="0 0 12 12"><circle cx="6" cy="6" r="5" fill="none" stroke="var(--gold)" stroke-width="1.4"/><path d="M6 3v3.5h2.5" fill="none" stroke="var(--gold)" stroke-width="1.2"/></svg>Monday - Friday: 8am until<br>18:00pm</li>
  </ul></div>

  <div class="abs rule" style="top:366px"></div>
</footer>
<div class="abs copy" style="color:var(--footer-text)">Copyright © 2016 by <em>veloraskinclinic</em>. All Rights Reserved.</div>
<div class="abs pay" role="img" aria-label="Accepted payment methods"><i></i><i></i><i></i><i></i><i></i></div>

</body>
</html>
```